Flyer for our prophetic church event

I need a flyer designed for the launching of our "7 Radiant Harvest Gatherings" event. This event should high light the next 7 Sundays starting on February the 11th, 2018

Event Name:
7 Radiant Harvests

Event Slogan or topic:
Go and tell John ... the blind see, the lame walk, the lepers are cleansed, the deaf hear, the dead are raised,
the poor have the gospel preached to them.

Speaker:
Prophet Marcus Obuya

February 11th
February 18th
February 25th
March 4th
March 11th
March 18th
March 25th

Location:
Talvor Community Center
382 Wendle Street
Portland, ME 04981
United States

Time:
10:00AM - 12:00PM

We welcome you all in the name of Jesus Christ

Contact Info:
Tel:+1(555) 302 1189 - Email:contact@mirovalefold.org - Website: http://velosa.org

Target Market(s)

Young adults

Industry/Entity Type

Church

Font styles to use
Other font styles liked:
• Surprise me, I trust the designers skills

Colors

Designer to choose colors to be used in the design.

Requirements
Must have
• The Velosa logo
• Marcus Obuya's picture
• The
Should not have
• The background of the Marcus Obuya's picture

```html
<!DOCTYPE html>
<html lang="en">
<head>
<meta charset="utf-8">
<title>7 Radiant Harvests – Velosa</title>
<link rel="stylesheet" href="https://fonts.googleapis.com/css2?family=Lobster&family=Raleway:wght@400;600;700;800&family=Lato:wght@400;700&family=Quicksand:wght@600;700&display=swap">
<style>
  :root{
    --navy:#0f4d7c;
    --orange:#f7941d;
    --white:#ffffff;
    --ink:#3d3d3d;
    --muted:#6b6b6b;
    --bar:#dcdcdc;
    --paper:#f7f7f7;
  }
  *{margin:0;padding:0;box-sizing:border-box}
  html,body{width:999px;height:1200px;overflow:hidden;background:var(--white)}
  .flyer{position:relative;width:999px;height:1200px;overflow:hidden;background:var(--paper);font-family:'Raleway',sans-serif}
  .hero-scene{position:absolute;left:0;top:0;width:999px;height:760px;
    background:
      radial-gradient(ellipse 560px 170px at 820px 640px,#140805 0%,#140805 58%,rgba(20,8,5,0) 64%),
      radial-gradient(ellipse 420px 170px at 480px 470px,rgba(255,190,80,.8),rgba(255,190,80,0) 70%),
      linear-gradient(180deg,#1e1210 0%,#4a2215 20%,#9a3f18 42%,#d8732a 60%,#b8521c 72%,#2a140c 88%,#120806 100%);}
  .shapes{position:absolute;left:0;top:0;width:999px;height:1200px}
  .column-shade{position:absolute;left:540px;top:640px;width:30px;height:420px;
    background:linear-gradient(90deg,rgba(0,0,0,0),rgba(0,0,0,.06))}

  .brand{position:absolute;left:64px;top:70px;display:flex;align-items:center;gap:14px}
  .brand-dot{width:20px;height:20px;border-radius:50%;background:var(--orange)}
  .brand-name{font-weight:600;font-size:56px;letter-spacing:2px;color:var(--white);line-height:1}

  .title{position:absolute;left:58px;top:188px;color:var(--white);font-weight:400}
  .title-number{position:absolute;left:0;top:0;font-weight:800;font-size:124px;line-height:1}
  .title-name{position:absolute;left:90px;top:4px;font-family:'Lobster',cursive;font-size:58px;white-space:nowrap;line-height:1.1}
  .title-start{position:absolute;left:98px;top:82px;font-weight:700;font-size:23px;white-space:nowrap}
  .title-start sup{font-size:12px}

  .info{position:absolute;left:76px;color:var(--white);display:flex;gap:14px;align-items:flex-start}
  .info svg{flex:none}
  .info-venue{top:330px}
  .info-time{top:380px;align-items:center}
  .venue-name{font-weight:700;font-size:14px;text-transform:uppercase;letter-spacing:.3px}
  .venue-address{font-size:14px;margin-top:3px}
  .time-text{font-weight:700;font-size:14px}

  .speaker-photo{position:absolute;left:96px;top:408px;width:256px;height:256px;border-radius:50%;
    border:7px solid var(--white);box-shadow:0 0 0 4px var(--orange),0 6px 16px rgba(0,0,0,.35);
    background:radial-gradient(circle at 50% 40%,#e9e4df 0%,#c9c0b8 60%,#8d8680 100%)}
  .speaker{position:absolute;left:420px;top:548px;color:var(--white)}
  .speaker-label{font-size:30px;font-weight:400;line-height:1.2}
  .speaker-name{font-size:32px;color:var(--orange);letter-spacing:.5px;margin-top:4px;line-height:1.2}
  .speaker-name strong{font-weight:800}
  .speaker-name span{font-weight:400}

  .topic{position:absolute;left:62px;top:800px;width:470px}
  .topic-heading{font-size:30px;color:var(--navy);line-height:1.2}
  .topic-heading strong{font-weight:800}
  .topic-heading span{font-weight:400}
  .topic-text{font-family:'Lato',sans-serif;font-size:14px;color:var(--muted);line-height:1.45;margin-top:12px}

  .welcome{position:absolute;left:64px;top:948px;font-family:'Lato',sans-serif;font-weight:700;color:var(--ink)}
  .welcome-line{font-size:28px;line-height:1.25;white-space:nowrap}
  .welcome-line em{font-style:normal;color:var(--orange)}

  .dates{position:absolute;left:600px;top:668px;width:320px;text-align:center}
  .dates-heading{font-family:'Quicksand',sans-serif;font-weight:700;font-size:28px;color:var(--navy);line-height:1.2;margin-bottom:12px}
  .dates-list{list-style:none}
  .dates-list li{font-family:'Quicksand',sans-serif;font-weight:700;font-size:24px;color:var(--ink);height:38px;line-height:38px;margin-bottom:2px}
  .dates-list li:nth-child(odd){background:var(--bar)}
  .dates-list sup{font-size:12px;vertical-align:9px}

  .contact{position:absolute;left:90px;top:1108px;display:flex;align-items:flex-end;gap:22px;color:var(--white);font-family:'Lato',sans-serif}
  .contact-lead{font-weight:700;font-size:20px;line-height:1.3;white-space:nowrap}
  .contact-item{display:flex;align-items:center;gap:7px;font-size:15px;white-space:nowrap;padding-bottom:4px}
</style>
</head>
<body>
<main class="flyer">
  <div class="hero-scene" role="img" aria-label="Sunset sky over a hill with a wooden cross draped in purple cloth"></div>

  <svg class="shapes" viewBox="0 0 999 1200" aria-hidden="true">
    <path d="M0 740 L0 640 Q20 520 150 496 L900 566 Q999 580 999 670 V1200 H0 Z" fill="var(--navy)"/>
    <path d="M0 742 L700 622 Q860 596 930 612 Q999 632 999 720 V1200 H0 Z" fill="var(--paper)"/>
    <path d="M0 742 L700 622 Q800 606 870 604" fill="none" stroke="var(--orange)" stroke-width="7"/>
    <path d="M130 1058 L999 1052" stroke="var(--orange)" stroke-width="6"/>
    <path d="M60 1200 Q70 1072 190 1068 L999 1062 V1200 Z" fill="var(--navy)"/>
  </svg>
  <div class="column-shade"></div>

  <div class="brand"><span class="brand-dot"></span><span class="brand-name">VELOSA</span></div>

  <h1 class="title">
    <span class="title-number">7</span>
    <span class="title-name">Radiant Harvests</span>
    <span class="title-start">Starting on February the 11<sup>TH</sup>, 2018</span>
  </h1>

  <div class="info info-venue">
    <svg width="22" height="30" viewBox="0 0 22 30"><path d="M11 2a8 8 0 0 0-8 8c0 6 8 14 8 14s8-8 8-14a8 8 0 0 0-8-8z" fill="none" stroke="#fff" stroke-width="2"/><circle cx="11" cy="10" r="3" fill="#fff"/><ellipse cx="11" cy="27" rx="8" ry="2" fill="none" stroke="#fff" stroke-width="1.5"/></svg>
    <div>
      <div class="venue-name">Talvor Community Center</div>
      <div class="venue-address">382 Wendle Street, Portland, ME 04981, United States</div>
    </div>
  </div>
  <div class="info info-time">
    <svg width="22" height="20" viewBox="0 0 22 20"><rect x="1" y="3" width="20" height="16" rx="2" fill="none" stroke="#fff" stroke-width="2"/><rect x="1" y="3" width="20" height="5" fill="#fff"/><path d="M5 11h2M10 11h2M15 11h2M5 15h2M10 15h2" stroke="#fff" stroke-width="2"/></svg>
    <div class="time-text">10:00AM - 12:00PM</div>
  </div>

  <div class="speaker-photo" role="img" aria-label="Portrait of speaker Marcus Obuya"></div>
  <div class="speaker">
    <div class="speaker-label">Speaker:</div>
    <div class="speaker-name"><strong>MARCUS</strong> <span>OBUYA</span></div>
  </div>

  <section class="topic">
    <h2 class="topic-heading"><strong>EVENT</strong> <span>TOPIC:</span></h2>
    <p class="topic-text">Go and tell John ... the blind see, the lame walk, the lepers are cleansed, the deaf hear, the dead are raised, the poor have the gospel preached to them.</p>
  </section>

  <div class="welcome">
    <div class="welcome-line">WE WELCOME YOU ALL IN</div>
    <div class="welcome-line">The name of <em>JESUS CHRIST</em></div>
  </div>

  <section class="dates">
    <h2 class="dates-heading">Event Dates:</h2>
    <ul class="dates-list">
      <li>11<sup>TH</sup> February</li>
      <li>18<sup>TH</sup> February</li>
      <li>25<sup>TH</sup> February</li>
      <li>4<sup>TH</sup> March</li>
      <li>11<sup>TH</sup> March</li>
      <li>18<sup>TH</sup> March</li>
      <li>25<sup>TH</sup> March</li>
    </ul>
  </section>

  <footer class="contact">
    <div class="contact-lead">For Registration or more details<br>CONTACT US :</div>
    <div class="contact-item">
      <svg width="16" height="16" viewBox="0 0 16 16"><path d="M3 1l3 3-2 2c1 2 3 4 5 5l2-2 3 3-2 3C6 15 1 10 1 3z" fill="var(--orange)"/></svg>
      +1(555) 302 1189
    </div>
    <div class="contact-item">
      <svg width="16" height="16" viewBox="0 0 16 16"><circle cx="8" cy="8" r="7" fill="none" stroke="var(--orange)" stroke-width="1.5"/><path d="M1 8h14M8 1c-3 4-3 10 0 14M8 1c3 4 3 10 0 14" fill="none" stroke="var(--orange)" stroke-width="1.2"/></svg>
      www.velosa.org
    </div>
    <div class="contact-item">
      <svg width="20" height="14" viewBox="0 0 20 14"><rect x="1" y="1" width="18" height="12" fill="none" stroke="var(--orange)" stroke-width="1.5"/><path d="M1 1l9 7 9-7" fill="none" stroke="var(--orange)" stroke-width="1.5"/></svg>
      contact@mirovalefold.org
    </div>
  </footer>
</main>
</body>
</html>
```